Wealth Education Business Needs Sharp Business Card Design

We need a business card design for a recently launched investor education business called Harbor Crest.

The final design should promote security, empowerment, self improvement and financial gain. The card will ideally promote the stature of the business.

For more information and colours please visit harborcrest.com.au

Target Market(s)

Corporate executives and high net worth individuals

Industry/Entity Type

Education

Contact Information for Business Card

Name
Position
Contact Address
Phone
Mobile
Email
Website

```html
<!DOCTYPE html>
<html lang="en">
<head>
<meta charset="utf-8">
<title>Harbor Crest — Business Card</title>
<link rel="stylesheet" href="https://fonts.googleapis.com/css2?family=Lato:wght@400;700&display=swap">
<style>
  :root {
    --backdrop: #e4e5e8;
    --navy: #1e2b40;
    --navy-deep: #18233a;
    --paper: #ffffff;
    --ink: #1b2436;
    --ink-soft: #4a4f57;
    --wordmark-dark: #3a3a3c;
    --accent: #1f8f8a;
    --swoosh: #6b6d72;
  }
  * { margin: 0; padding: 0; box-sizing: border-box; }
  html, body {
    width: 1200px; height: 960px; overflow: hidden;
    background: var(--backdrop);
    font-family: "Lato", sans-serif;
  }
  .card {
    position: absolute; left: 271px; width: 644px; height: 368px;
    box-shadow: 0 6px 18px rgba(0,0,0,0.18);
    overflow: hidden;
  }
  /* Front */
  .card--front { top: 84px; }
  .front-texture {
    position: absolute; inset: 0;
    background: radial-gradient(ellipse at 50% 50%, #26344c 0%, var(--navy) 55%, var(--navy-deep) 100%);
  }
  .brand {
    position: absolute; display: flex; align-items: center; gap: 18px;
    font-weight: 400; text-transform: uppercase; letter-spacing: 0.16em;
  }
  .brand__dot {
    width: 14px; height: 14px; border-radius: 50%; background: var(--accent); flex: none;
  }
  .card--front .brand {
    left: 0; right: 0; top: 160px; justify-content: center;
    font-size: 40px; color: var(--paper);
  }
  .front-url {
    position: absolute; left: 0; right: 0; top: 302px; text-align: center;
    color: var(--paper); font-size: 15px;
  }
  /* Back */
  .card--back { top: 508px; background: var(--paper); }
  .person { position: absolute; left: 63px; top: 61px; }
  .person__name { font-weight: 700; font-size: 19px; color: var(--ink); }
  .person__role { font-size: 15px; color: var(--ink-soft); margin-top: 1px; }
  .address {
    position: absolute; left: 63px; top: 168px;
    font-size: 15px; line-height: 19px; color: var(--ink-soft); font-style: normal;
  }
  .contacts { position: absolute; left: 58px; top: 227px; list-style: none; }
  .contacts li {
    display: flex; align-items: center; gap: 12px;
    font-size: 15px; line-height: 20.5px; color: var(--ink-soft);
  }
  .contacts svg { width: 16px; height: 16px; flex: none; fill: var(--ink); }
  .card--back .brand {
    left: 308px; top: 134px; font-size: 32px; color: var(--wordmark-dark); gap: 14px;
  }
  .card--back .brand__dot { width: 12px; height: 12px; }
  .back-band { position: absolute; left: 0; top: 0; width: 644px; height: 368px; }
  .back-url {
    position: absolute; right: 59px; top: 327px;
    color: var(--paper); font-size: 15px;
  }
</style>
</head>
<body>
  <section class="card card--front">
    <div class="front-texture" role="img" aria-label="Subtle navy pattern of vertical rounded bars"></div>
    <div class="brand"><span class="brand__dot"></span>Harbor Crest</div>
    <div class="front-url">www.harborcrest.com.au</div>
  </section>

  <section class="card card--back">
    <svg class="back-band" viewBox="0 0 644 368" aria-hidden="true">
      <path d="M0 320 C 120 345, 250 345, 400 310 C 500 288, 590 282, 644 290 L644 368 L0 368 Z" fill="var(--navy)"/>
      <path d="M28 322 C 160 340, 280 322, 420 296 C 520 278, 600 278, 644 290 C 590 283, 510 290, 420 306 C 300 328, 170 344, 28 322 Z" fill="var(--swoosh)"/>
    </svg>

    <div class="person">
      <div class="person__name">Daniel Whitford</div>
      <div class="person__role">Founder &amp; CEO</div>
    </div>

    <address class="address">Level 4, 72 Quayside Street<br>Southport QLD 4215</address>

    <ul class="contacts">
      <li><svg viewBox="0 0 16 16"><path d="M1 5c0-2 3-3 7-3s7 1 7 3v1h-3V5H4v1H1z M4 7h8l2 6H2z"/></svg>1300.418.562</li>
      <li><svg viewBox="0 0 16 16"><path d="M4 0h8a1 1 0 0 1 1 1v14a1 1 0 0 1-1 1H4a1 1 0 0 1-1-1V1a1 1 0 0 1 1-1zm1 2v10h6V2zm3 11a1 1 0 1 0 0 2 1 1 0 0 0 0-2z"/></svg>0000.000.000</li>
      <li><svg viewBox="0 0 16 16"><path d="M1 3h14v10H1zm1.5 1.5v.3L8 9l5.5-4.2v-.3zm0 2.2v4.8h11V6.7L8 10.8z"/></svg>support@harborcrest.com.au</li>
    </ul>

    <div class="brand"><span class="brand__dot"></span>Harbor Crest</div>

    <div class="back-url">www.harborcrest.com.au</div>
  </section>
</body>
</html>
```